Business card design reauest

2 sided. White on both sides

Martin Oakhurst

Cedar Bay, Westmark

Cell Phone / Chatrly/ Talkon/Pingo
1-555-382-7194
Moakhurst@kvpartsline.vn
Www.kvpartsline.vn
Www.kvpartsline.com

Industry/Entity Type

Sofa and furniture and kitchen

Contact Information for Business Card

2 sided. White on both sides Martin Oakhurst Cedar Bay, Westmark Cell Phone / Chatrly/ Talkon/Pingo 1-555-382-7194 Moakhurst@kvpartsline.vn Www.kvpartsline.vn Www.kvpartsline.com

```html
<!DOCTYPE html>
<html lang="en">
<head>
<meta charset="utf-8">
<title>KV Partsline – Business Card</title>
<link rel="stylesheet" href="https://fonts.googleapis.com/css2?family=Cinzel:wght@500&family=Poppins:wght@400;500;700&display=swap">
<style>
  :root {
    --stage: #707070;
    --paper: #ffffff;
    --green: #069833;
    --ink: #222222;
    --rule: #e4e4e4;
  }
  * { box-sizing: border-box; margin: 0; padding: 0; }
  html, body { width: 934px; height: 1200px; overflow: hidden; }
  body { background: var(--stage); position: relative; font-family: "Poppins", sans-serif; color: var(--ink); }

  .card {
    position: absolute; left: 103px; width: 729px; height: 456px;
    background: var(--paper); overflow: hidden;
    box-shadow: 0 2px 6px rgba(0,0,0,.35);
  }
  .card--front { top: 100px; }
  .card--back { top: 633px; }

  .card__footer { position: absolute; left: 0; bottom: 0; width: 729px; height: 19px; }

  .brand-name {
    position: absolute; font-family: "Cinzel", serif; font-weight: 500;
    color: var(--green); white-space: nowrap; text-align: center; line-height: 1.2;
  }
  .card--front .brand-name { left: 0; width: 729px; top: 255px; font-size: 58px; letter-spacing: 1px; }
  .card--back .brand-name { left: 20px; width: 280px; top: 252px; font-size: 31px; }

  .contact-panel { position: absolute; inset: 0; }
  .holder-name {
    position: absolute; left: 325px; width: 373px; top: 98px; text-align: center;
    font-weight: 700; font-size: 38px; line-height: 1.3; color: var(--green); white-space: nowrap;
  }
  .location {
    position: absolute; left: 332px; width: 359px; top: 168px; display: flex; justify-content: center;
    align-items: center; gap: 8px; font-weight: 700; font-size: 21px; line-height: 1.3; color: var(--ink);
  }
  .channels {
    position: absolute; left: 332px; width: 359px; top: 214px; text-align: center;
    font-size: 15px; line-height: 1.3; white-space: nowrap;
  }
  .contact-list { position: absolute; left: 368px; top: 248px; width: 302px; list-style: none; }
  .contact-list li {
    height: 37px; display: flex; align-items: center;
    border-bottom: 1px solid var(--rule); font-size: 17.5px; white-space: nowrap;
  }
  .contact-list li:last-child { border-bottom: none; }
  .contact-list .phone-number { font-weight: 500; }
  .contact-icon {
    width: 26px; height: 37px; background: var(--ink); flex: none;
    display: flex; align-items: center; justify-content: center; margin-right: 18px;
  }
  .contact-list li:first-child .contact-icon { border-radius: 6px 6px 0 0; }
  .contact-list li:last-child .contact-icon { border-radius: 0 0 6px 6px; }
</style>
</head>
<body>

<section class="card card--front">
  <div class="brand-name">KV Partsline</div>
  <svg class="card__footer" viewBox="0 0 729 19">
    <polygon points="0,0 221,0 231,19 0,19" fill="#222"/>
    <polygon points="504,0 729,0 729,19 494,19" fill="#222"/>
    <polygon points="231,8 494,8 489,19 236,19" fill="#069833"/>
  </svg>
</section>

<section class="card card--back">
  <svg class="contact-panel" viewBox="0 0 729 456" aria-hidden="true">
    <rect x="511" y="0" width="218" height="456" fill="#069833"/>
    <rect x="325" y="30" width="373" height="426" fill="#069833"/>
    <rect x="332" y="37" width="359" height="419" fill="#ffffff"/>
  </svg>

  <div class="brand-name">KV Partsline</div>

  <h1 class="holder-name">Martin Oakhurst</h1>
  <p class="location">
    <svg width="16" height="24" viewBox="0 0 16 24"><path d="M8 0C3.6 0 0 3.5 0 7.9 0 13.5 8 24 8 24s8-10.5 8-16.1C16 3.5 12.4 0 8 0z" fill="#222"/><circle cx="8" cy="8" r="3" fill="#fff"/></svg>
    Cedar Bay, Westmark
  </p>
  <p class="channels">Cell Phone | Chatrly | Talkon | Pingo</p>
  <ul class="contact-list">
    <li><span class="contact-icon"><svg width="14" height="14" viewBox="0 0 24 24"><path d="M6.6 10.8a15.1 15.1 0 0 0 6.6 6.6l2.2-2.2c.3-.3.7-.4 1-.2 1.1.4 2.3.6 3.6.6.6 0 1 .4 1 1V20c0 .6-.4 1-1 1C10.6 21 3 13.4 3 4c0-.6.4-1 1-1h3.5c.6 0 1 .4 1 1 0 1.3.2 2.5.6 3.6.1.3 0 .7-.2 1z" fill="#069833"/></svg></span><span class="phone-number">1-555-382-7194</span></li>
    <li><span class="contact-icon"><svg width="14" height="12" viewBox="0 0 24 20"><rect x="1" y="2" width="22" height="16" rx="2" fill="#069833"/><path d="M2 4l10 7 10-7" stroke="#222" stroke-width="2" fill="none"/></svg></span>Moakhurst@kvpartsline.vn</li>
    <li><span class="contact-icon"><svg width="14" height="14" viewBox="0 0 24 24"><circle cx="12" cy="12" r="10" fill="none" stroke="#069833" stroke-width="2.2"/><path d="M2 12h20M12 2c3 3 3 17 0 20M12 2c-3 3-3 17 0 20" stroke="#069833" stroke-width="2" fill="none"/></svg></span>Www.kvpartsline.vn</li>
    <li><span class="contact-icon"><svg width="14" height="14" viewBox="0 0 24 24"><circle cx="12" cy="12" r="10" fill="none" stroke="#069833" stroke-width="2.2"/><path d="M2 12h20M12 2c3 3 3 17 0 20M12 2c-3 3-3 17 0 20" stroke="#069833" stroke-width="2" fill="none"/></svg></span>Www.kvpartsline.com</li>
  </ul>

  <svg class="card__footer" viewBox="0 0 729 19">
    <polygon points="0,0 377,0 387,19 0,19" fill="#222"/>
    <polygon points="660,0 729,0 729,19 650,19" fill="#222"/>
    <polygon points="387,8 650,8 645,19 392,19" fill="#069833"/>
  </svg>
</section>

</body>
</html>
```